Leading the way in online fitness and education requires power house web design

If you need to contact me you can do so via
skype: Travlin

We need a website designed for new company based in Houston Texas called "TravlinFit". We offer web based training and nutrition programs for our members for example we use the same software as these companies: http://marobelka.com/ http://www.liftquorra.com/ i would like my visitors to be captivated by the level of design creativity of the site.

colors to use would be grey, orange and green.
for example i like the green of this site http://www.cartbeam.com/
i will upload my logo files so you can get a feel for shades of grey and orange.

there is a 3d effect filter i would like applied to my logo for use in the web design i have uploaded what that effect looks like.

i will need your designs to be complete with all interior pages which will include Home, Fitness, Nutrition, Fit Lounge, Fit Score, Fit School, Contact Us, Sign up.

fit lounge on my site is the same as pathwick on liftquorra and locker room on marobelka just re branded.

fit school is a research corner for members to learn about health and fitness, we are members of major medical journals on health and fitness and will have all our articles be from the newest research findings.

competitor sites
these sites use same software:
http://marobelka.com/
http://www.liftquorra.com/

these sites are other software.
http://home.sprintmesa.com/software-for-athletes.aspx
http://www.vigordex.com/

here are some websites that i like:
http://www.crestwaveplay.com/
http://www.nub-lantern.com/
http://fimzol.com/
http://www.parqudo.com/
http://www.lortavi.de/fandiloop/
http://brisketmade.com/

i also like the greens in this site that i am uploading

I have been reviewing the designs and would like to update everyone at once I do not want a normal fitness website design style, no testimonials, blog post, bodyfat calculator

my website will be a membership based website. i want the website to sell the main points of my fitness app that my members will have access to look at the comments for my selling points, use those points in the site create designs and graphics to visualize those points.

look at these sites and gain inspiration

http://www.tuvelo.com.pl/#/projekty/case-studies
http://www.quendar.com/en#/home#ld-kpvm-402617-0045
http://www.nub-lantern.com/
http://fimzol.com/
http://www.parqudo.com/

i have a few designers asking me what the selling points are, the website needs to be built around these points

main selling points.

overview

programs utilize the best multi-joint exercises combined with high intensity cardio, to give you a full-body workout, efficiently and effectively. This means you’re burning more calories and building more lean muscle per unit of time than traditional weight training and cardio programs.

When you sign up, you''ll receive a work out and diet plan to fit your goals and fitness level. As you progress through your plan, you can use the personal fitness and meal calendar to record your results. When you sign-up we''ll ask you a series of questions and your workouts will be tailored to your exact needs. That means never having to use a generic diet and exercise plan again.

If you''ve ever tried to lose weight and build muscle and didn''t succeed, we feel your pain. Until now, trying to navigate all the fitness fads and latest trends on your own has been difficult. The best option - hiring a certified personal trainer - may be out of your financial reach. That''s where we come in - we''re personal trainers on a mission to help you reach your fitness goals quickly and for less money than in person training. Best of all, we''re here to help you day or night.

Fitness

Personal Fitness Calendar

Tailored to the member’s schedule and flexible to accommodate any changes to a member’s regular fitness schedule. Track your progress and stay on track with your fitness goals.

Custom Fitness Plan

Based on a member’s current physical condition and goals.

• Step by step exercise instructions
• 3-D video demonstrations of over 600 exercises, including functional and body-weight only movements
• Equipment filter can customize plans to your gym’s equipment package
• Record workouts to track exercise history and progression

Nutrition

Nutritional Assessment

Daily recommended caloric intake (Protein, Carbohydrates and Fats), based on personal profile and daily fitness plan.

Custom Meal Plan

Personalized meal plan based on nutritional assessment.

• Choose number of meals per day
• Add dietary restrictions, food preferences or dislikes
• Database of thousands of ingredients allows for hundreds of thousands of meal combinations
• Include favorite foods by entering custom nutritional information

Weight tracking

Calculate goal weight and track weight-loss or weight-gain progress. You will reach your goals in no time.

Fit Lounge

What is the most important part of any workout or fitness program? Staying motivated. And what better form of motivation than positive encouragement from your peers?

Fit Lounge is fitness focused social network for health-minded individuals looking for a simple and convenient place to track their workout goals and monitor their progress. A unique system of motivation, support and accountability makes setting fitness goals and then keeping up with them easy

Track

Start by setting fitness goals that you want to track. They can be anything from running and jogging to how many hours of sleep you are getting and how many glasses of water you are drinking every day. Other members of the travlinfits community might be tracking the same workout goals as you, so you can always join their groups as well.

Share

Once you start tracking your workout goals, you can share your progress with your friends. Reach a new max on your bench press? Let everyone know. Eclipse the 10 mile mark on your daily run? Spread the word! The communication of encouragement back and forth is a great way to ensure that everyone stays on track with their workout goals.

Achieve

Of course, the point of any workout or fitness program is to achieve the goals you’ve set. And with help from travlinfits workout tracking tools and encouragement from the community, you will achieve your workout goals in no time. When you see a friend has achieved his or her fitness goals, you can send them a virtual “fist bump” as a sign of congratulations. The number of “fist bumps” each user accumulates will be displayed on their profile, providing additional motivation and a healthy dose of competition.

Reason: i dont feel the designs i have received are of the quality i am looking for

check this website out, i know its flash, but i also know you can get creative without flash and have nice effects throughout the site.

http://www.driftlane-hub.com/

I dont want plain jane designs, insert the content i provided into the site and have it explored in a unique way. take as much time on the design as you need as i will keep extending deadline until i find one that is perfect.

as said before don't make the site anything like the competition sites, its only purpose is to sell the memberships using content provided so i need an innovative way to for them to explore that content,

as your designing this site add me on skype so i can detail and help brainstorm ideas my skype id is travlin
you can stray from the color scheme a little or throw it away if you want i just want to see how creative you can get.

Industry/Entity Type

School

Requirements
Nice to have
• if you notice at the bottom of http://marobelka.com/ she has the orange bar with the three short content parts, i like the idea of having a space like that for similar content.

on http://www.vigordex.com/ if you look to the left side of the scrolling icons i like the idea of having icons or animated pictures to point of key benefits.

```html
<!DOCTYPE html>
<html lang="en">
<head>
<meta charset="utf-8">
<title>TravlinFit</title>
<link rel="stylesheet" href="https://fonts.googleapis.com/css2?family=PT+Sans:wght@400;700&family=Ubuntu:wght@400;500;700&family=Cousine&display=swap">
<style>
  :root {
    --green: #72bb22;
    --green-deep: #4d9f0c;
    --green-light: #d5ef9c;
    --green-link: #3f8a0c;
    --nav-text: #2f4412;
    --nav-accent: #6e1212;
    --blue-head: #1e66b1;
    --blue-sub: #1565a8;
    --text: #3a3a3a;
    --panel: #ffffff;
    --panel-line: #dadada;
    --bar-bg: #f4f4f4;
    --footer-text: #3f5f85;
    --logo-ink: #2f2f2f;
    --logo-accent: #ef5a14;
    --hero-top: #b6dc86;
    --hero-bottom: #3c6cc0;
  }
  * { box-sizing: border-box; margin: 0; padding: 0; }
  html, body { width: 1200px; height: 948px; overflow: hidden; }
  body {
    position: relative;
    font-family: "PT Sans", Arial, sans-serif;
    color: var(--text);
    background: linear-gradient(#f6f6f6, #e6e6e6);
  }
  .header {
    position: absolute; left: 0; top: 0; width: 1200px; height: 322px;
    background:
      radial-gradient(ellipse 300px 280px at 300px 130px, var(--green-light), rgba(213,239,156,0) 100%),
      linear-gradient(var(--green) 0%, #79c02a 100%);
    border-top: 8px solid var(--green-deep);
  }
  .hero-photo {
    position: absolute; z-index: 2; left: 102px; top: 8px; width: 284px; height: 309px;
    background: linear-gradient(180deg, var(--hero-top) 0%, #8fb9b0 45%, var(--hero-bottom) 100%);
  }
  .search {
    position: absolute; left: 893px; top: 30px; width: 211px; height: 26px;
    background: #f1f6ea; border: 1px solid #9fce6a; border-radius: 13px;
    box-shadow: inset 0 1px 2px rgba(0,0,0,.15);
  }
  .search-placeholder {
    position: absolute; left: 14px; top: 4px; font-size: 13px; font-style: italic; color: #9a9a9a;
  }
  .search-button {
    position: absolute; right: -1px; top: -1px; width: 33px; height: 26px;
    background: linear-gradient(#6bb52a, #4b9611); border-radius: 0 13px 13px 0;
  }
  .search-button svg { position: absolute; left: 10px; top: 6px; }
  .brand {
    position: absolute; left: 418px; top: 70px; display: flex; align-items: center; gap: 14px;
  }
  .brand-mark { width: 58px; height: 58px; border-radius: 50%; background: var(--logo-accent); }
  .brand-name {
    font-family: "Ubuntu", sans-serif; font-weight: 700; font-size: 50px; color: var(--logo-ink); letter-spacing: -0.5px;
  }
  .main-nav {
    position: absolute; left: 55px; top: 212px; width: 1049px; height: 52px;
    background: linear-gradient(#ffffff, #f1f1f1); border: 1px solid #cfd8c4; border-radius: 8px;
  }
  .nav-link {
    position: absolute; top: 15px; font-family: "Ubuntu", sans-serif; font-weight: 500; font-size: 16px; color: var(--nav-text);
  }
  .nav-link.accent { color: var(--nav-accent); }
  .content-panel {
    position: absolute; left: 88px; top: 328px; width: 1042px; height: 507px;
    background: var(--panel); border: 1px solid var(--panel-line); border-radius: 8px;
  }
  .section-title {
    position: absolute; font-family: "Ubuntu", sans-serif; font-weight: 500; font-size: 17px; color: var(--blue-head);
  }
  .rule-h { position: absolute; left: 108px; top: 380px; width: 1006px; height: 1px; background: #8cc251; }
  .rule-v { position: absolute; left: 789px; top: 380px; width: 1px; height: 215px; background: #8cc251; }
  .welcome-photo {
    position: absolute; left: 108px; top: 409px; width: 160px; height: 135px;
    background: radial-gradient(circle at 40% 50%, #6fc1f6, #1c67c4 70%, #0f4ca0);
  }
  .welcome-copy {
    position: absolute; left: 280px; top: 402px; width: 416px; font-size: 12px; line-height: 19px; color: var(--text);
  }
  .welcome-copy .lead { color: var(--blue-sub); font-weight: 700; font-size: 13px; }
  .welcome-copy a { color: var(--green-link); text-decoration: underline; }
  .welcome-copy p + p { margin-top: 19px; }
  .services { position: absolute; left: 857px; top: 397px; font-size: 12px; line-height: 19.1px; }
  .services .lead { color: var(--blue-sub); font-weight: 700; font-size: 13px; }
  .services li { list-style: none; color: var(--green-link); }
  .services li::before { content: "\2022"; margin-right: 4px; color: var(--green-link); }
  .services li span { text-decoration: underline; }
  .gallery-bar {
    position: absolute; left: 100px; top: 597px; width: 1018px; height: 50px;
    background: var(--bar-bg); border: 1px solid #d3d3d3; border-radius: 8px;
  }
  .gallery-arrow { position: absolute; top: 694px; }
  .gallery-photo { position: absolute; top: 663px; height: 144px; }
  .career { position: absolute; left: 868px; top: 669px; width: 220px; font-size: 12px; line-height: 19px; }
  .career h3 { color: var(--blue-sub); font-size: 13px; font-weight: 700; }
  .career p + h3 { margin-top: 16px; }
  .footer {
    position: absolute; left: 0; top: 850px; width: 1200px; height: 67px;
    background: #ededed; border-top: 1px solid #d2d2d2; border-bottom: 1px solid #d2d2d2;
  }
  .social-box { position: absolute; width: 31px; height: 31px; border-radius: 3px; }
  .social-box.first { left: 100px; top: 870px; background: #35b4e4; }
  .social-box.second { left: 143px; top: 873px; background: #3f5c95; }
  .follow { position: absolute; left: 185px; top: 877px; font-size: 14px; color: #3a78b8; }
  .footer-link { position: absolute; top: 876px; font-family: "Cousine", monospace; font-size: 13px; color: var(--footer-text); }
  .copyright { position: absolute; left: 0; top: 925px; width: 1268px; text-align: center; font-size: 11px; color: #6a6a6a; }
</style>
</head>
<body>
  <header class="header">
    <div class="search">
      <span class="search-placeholder">search...</span>
      <span class="search-button">
        <svg width="13" height="13" viewBox="0 0 13 13"><circle cx="5" cy="5" r="3.6" fill="none" stroke="#fff" stroke-width="1.8"/><line x1="7.6" y1="7.6" x2="12" y2="12" stroke="#fff" stroke-width="2"/></svg>
      </span>
    </div>
    <div class="brand">
      <span class="brand-mark"></span>
      <span class="brand-name">TravlinFit</span>
    </div>
  </header>

  <nav class="main-nav">
    <span class="nav-link" style="left:360px">Home</span>
    <span class="nav-link" style="left:423px">Fitness</span>
    <span class="nav-link" style="left:497px">Nutrition</span>
    <span class="nav-link" style="left:578px">Fit Lounge</span>
    <span class="nav-link" style="left:669px">Fit Score</span>
    <span class="nav-link" style="left:753px">Fit School</span>
    <span class="nav-link" style="left:837px">Contact Us</span>
    <span class="nav-link accent" style="left:932px">Sign up</span>
  </nav>

  <div class="hero-photo" role="img" aria-label="Photo of an athlete stretching on a blue exercise mat"></div>

  <main>
    <div class="content-panel"></div>
    <h2 class="section-title" style="left:129px;top:350px">WELCOME TO OUR WEB SITE</h2>
    <h2 class="section-title" style="left:857px;top:351px">SERVICES</h2>
    <div class="rule-h"></div>
    <div class="rule-v"></div>

    <div class="welcome-photo" role="img" aria-label="Glowing runner figure with a heartbeat line"></div>
    <div class="welcome-copy">
      <p><span class="lead">Lorem ipsum dolor sit amet, contuer adipiscingelit</span><br>
      sed diamaccusantium doloremque laudantium, totam rem aperiam eaquep. Store veritatis et quasi architecto <a>beatae vitae dicta sunt, explicabo</a> nemo enim ipsam voluptatem.<br>
      , quia voluptas sit, aspernatur aut odit aut fugit.</p>
      <p><strong>Duis autem vel eum iriure dolor</strong> in hendrerit in vvdolore eu feugiat nulla facilisis at vero eros et accumsan et iusto odio dignissim qui blandit.</p>
    </div>

    <div class="services">
      <p class="lead">Lorem Ipsum is simply dummy</p>
      <ul>
        <li><span>Lorem Ipsum has been the industry</span></li>
        <li><span>Standard dummy text ever since the </span></li>
        <li><span>Make a type specimen book.</span></li>
        <li><span>It has survived not only five centuries</span></li>
        <li><span>Lorem Ipsum has been the industry</span></li>
        <li><span>Standard dummy text ever since the </span></li>
        <li><span>Make a type specimen book.</span></li>
        <li><span>It has survived not only five centuries</span></li>
      </ul>
    </div>

    <div class="gallery-bar"></div>
    <h2 class="section-title" style="left:129px;top:612px">PHOTOGALLERY</h2>
    <h2 class="section-title" style="left:867px;top:612px">CAREER</h2>

    <svg class="gallery-arrow" style="left:129px" width="17" height="55" viewBox="0 0 17 55"><polygon points="17,0 17,55 0,27.5" fill="#7cc12f"/></svg>
    <svg class="gallery-arrow" style="left:760px" width="17" height="55" viewBox="0 0 17 55"><polygon points="0,0 0,55 17,27.5" fill="#7cc12f"/></svg>

    <div class="gallery-photo" style="left:157px;width:37px;background:linear-gradient(90deg,#efe4dc,#8c5f48)" role="img" aria-label="Athlete in profile"></div>
    <div class="gallery-photo" style="left:207px;width:219px;background:linear-gradient(#f3e6d4,#e0d4c6 60%,#bdb3a8)" role="img" aria-label="Group step aerobics class"></div>
    <div class="gallery-photo" style="left:439px;width:96px;background:linear-gradient(90deg,#d9eef6,#e9c7ad 50%,#eef3f6)" role="img" aria-label="Woman stretching by the sea"></div>
    <div class="gallery-photo" style="left:535px;width:118px;background:linear-gradient(#fafafa,#d9a887 45%,#2c2c2c)" role="img" aria-label="Fit man gesturing"></div>
    <div class="gallery-photo" style="left:667px;width:80px;background:linear-gradient(#b87b4d,#8f6a55 55%,#6b7ea1)" role="img" aria-label="Trainer assisting a floor exercise"></div>

    <div class="career">
      <h3>Lorem ipsum dolor sit amet</h3>
      <p>sed diamaccusantium doloremque laudan-<br>tium, totam rem aperiam eaquep.</p>
      <h3>Lorem ipsum dolor sit amet</h3>
      <p>sed diamaccusantium doloremque laudan-<br>tium, totam rem aperiam eaquep.</p>
    </div>
  </main>

  <footer>
    <div class="footer"></div>
    <span class="social-box first"></span>
    <span class="social-box second"></span>
    <span class="follow">Follow us</span>
    <span class="footer-link" style="left:321px">Home</span>
    <span class="footer-link" style="left:387px">Fitness</span>
    <span class="footer-link" style="left:473px">Nutrition</span>
    <span class="footer-link" style="left:568px">Fit Lounge</span>
    <span class="footer-link" style="left:670px">Fit Score</span>
    <span class="footer-link" style="left:768px">Fit School</span>
    <span class="footer-link" style="left:862px">Contact Us</span>
    <span class="footer-link" style="left:968px">Sign up</span>
    <p class="copyright">Copyright travlinfit 2012</p>
  </footer>
</body>
</html>
```